K.T.L Electrical Services Pty Ltd

Electrical contracting business. I have a base for the design which i like. The contact number needs to be changed to 0491736250 and the O made more solid and level with the rest of the letters. If you have any other ideas of what would make it better I'm happy to see them.

The back side to be written as dot points with the following:
- Residential & Commercial
- Maintenance
- PV & Battery servicing
- EV Chargers

```html
<!DOCTYPE html>
<html lang="en">
<head>
<meta charset="utf-8">
<title>K.T.L Electrical Services – Business Cards</title>
<link rel="stylesheet" href="https://fonts.googleapis.com/css2?family=Arimo:wght@400;700&display=swap">
<style>
  :root {
    --bg: #e4e4e4;
    --card-front: #000000;
    --card-back: #303030;
    --teal: #8aa9ab;
    --orange: #d98f55;
    --white: #ffffff;
    --muted: #8a8a8a;
    --rule: #8c8c8c;
    --emboss: #4c4c4c;
  }
  * { margin: 0; padding: 0; box-sizing: border-box; }
  html, body {
    width: 1200px; height: 1200px; overflow: hidden;
    background: var(--bg);
    font-family: "Arimo", Arial, sans-serif;
  }
  .canvas { position: relative; width: 1200px; height: 1200px; }
  .card { position: absolute; overflow: hidden; }

  /* Front */
  .card-front { left: 270px; top: 170px; width: 671px; height: 383px; background: var(--card-front); }
  .brand-front {
    position: absolute; left: 372px; top: 70px; width: 276px;
    text-align: center; color: var(--teal);
  }
  .brand-name {
    display: flex; align-items: center; justify-content: center; gap: 10px;
    font-weight: 400; line-height: 1.2; white-space: nowrap;
  }
  .brand-front .brand-name { font-size: 22px; }
  .brand-mark { display: inline-block; border-radius: 50%; background: currentColor; }
  .brand-front .brand-mark { width: 20px; height: 20px; }
  .licence { font-weight: 400; }
  .brand-front .licence { font-size: 13px; margin-top: 8px; }

  .person { position: absolute; left: 47px; top: 216px; }
  .person-name { font-size: 27px; font-weight: 700; color: var(--teal); letter-spacing: 0.3px; }
  .person-role { font-size: 15px; color: var(--muted); margin-top: 2px; }

  .divider { position: absolute; left: 47px; top: 273px; width: 581px; height: 1px; background: var(--rule); }

  .contact { position: absolute; left: 45px; top: 283px; list-style: none; color: var(--white); font-size: 16px; }
  .contact li { display: flex; align-items: center; gap: 9px; height: 20px; }
  .contact svg { width: 14px; height: 14px; fill: var(--teal); }

  .address {
    position: absolute; right: 43px; top: 286px;
    text-align: right; color: var(--white); font-size: 16px; line-height: 21px; font-style: normal;
  }
  .bands { position: absolute; left: 0; bottom: 0; width: 671px; height: 33px; }
  .website { position: absolute; right: 43px; bottom: 7px; font-size: 15px; color: #111; }

  /* Back */
  .card-back { left: 262px; top: 653px; width: 687px; height: 393px; background: var(--card-back); }
  .brand-back {
    position: absolute; left: 0; top: 110px; width: 100%;
    text-align: center; color: var(--emboss);
  }
  .brand-back .brand-name { font-size: 40px; gap: 16px; }
  .brand-back .brand-mark { width: 36px; height: 36px; }
  .brand-back .licence { font-size: 21px; margin-top: 14px; }

  .services {
    position: absolute; left: 0; top: 305px; width: 100%;
    color: var(--white); font-size: 18px; line-height: 22px; text-align: center;
  }
  .services p { display: flex; justify-content: center; align-items: center; gap: 14px; }
  .services .bullet { width: 7px; height: 7px; border-radius: 50%; background: var(--orange); }
</style>
</head>
<body>
<main class="canvas">

  <section class="card card-front" aria-label="Business card front">
    <div class="brand-front">
      <div class="brand-name"><span class="brand-mark"></span>K.T.L Electrical Services</div>
      <div class="licence">EC 20417</div>
    </div>

    <div class="person">
      <h1 class="person-name">DANIEL REEVES</h1>
      <p class="person-role">President</p>
    </div>

    <div class="divider"></div>

    <ul class="contact">
      <li>
        <svg viewBox="0 0 24 24" aria-hidden="true"><path d="M6.6 10.8a15.1 15.1 0 0 0 6.6 6.6l2.2-2.2a1 1 0 0 1 1-.25 11.4 11.4 0 0 0 3.6.57 1 1 0 0 1 1 1V20a1 1 0 0 1-1 1A17 17 0 0 1 3 4a1 1 0 0 1 1-1h3.5a1 1 0 0 1 1 1c0 1.25.2 2.45.57 3.57a1 1 0 0 1-.25 1z"/></svg>
        0491736250
      </li>
      <li>
        <svg viewBox="0 0 24 24" aria-hidden="true"><path d="M2 5h20v14H2z M3 6l9 7 9-7" fill="none" stroke="#8aa9ab" stroke-width="2"/></svg>
        info@KTL.com
      </li>
    </ul>

    <address class="address">4215 Wattle Grove Road<br>Brookfield, Canada 41826</address>

    <svg class="bands" viewBox="0 0 671 33" aria-hidden="true">
      <polygon points="0,17 416,17 405,33 0,33" fill="var(--orange)"/>
      <polygon points="432,0 671,0 671,33 404,33" fill="#000"/>
      <polygon points="435,0 671,0 671,33 409,33" fill="var(--teal)"/>
    </svg>
    <span class="website">www.KTL.com</span>
  </section>

  <section class="card card-back" aria-label="Business card back">
    <div class="brand-back">
      <div class="brand-name"><span class="brand-mark"></span>K.T.L Electrical Services</div>
      <div class="licence">EC 20417</div>
    </div>

    <div class="services">
      <p><span>Residential &amp; Commercial</span><span class="bullet"></span><span>Maintenance</span></p>
      <p><span>PV &amp; Battery servicing</span><span class="bullet"></span><span>EV Chargers</span></p>
    </div>
  </section>

</main>
</body>
</html>
```